Flyer für Onlineshop
Zielgruppe
Wir vertreiben 2 Komponentenlacke, wasserbasiert, auf Polyurethanharz Basis zur Sanierung von Fliesen vieles und mehr.
Aufgabenstellung
Wir möchten eine Fleyer speziell für die Fliesenfarben.
Das Design soll frisch, modern und ansprechend gestaltet sein. Wir möchten den Fleyer öffentlich auslegen aber auch an z.B Jugendherbergen, Kurhäuser ect. und privat Personen verteilen um darauf aufmerksam zu machen das es eine güstige alternative zum Neukauf gibt.
Auf dem Flyer soll in der Fliesenlack im Vordergrund stehen es darf aber kurz auf weitere Produkte aufmerksam gemacht werden.
für die Größe des Flyers habe ich keine genauen Vorstellungen lasse mich überraschen.
Sie finden die Informationen die Sie benötigen unter
www.ralbo-sonderlacke.com/farben-lacke/fliesenfarbe
Der Fleyer sollte die Maße DIN lang (105 x 210 mm) hoch / 4 Seiten
Aber auch andere Vorschläge sind Willkommen
Also Logo habe ich verschiedene jpg´s hochgeladen..leider ist die qualität nicht sehr gut aber vielleicht können Sie was damit anfangen.
Bei weiteren Fragen stehe ich Ihnen gerne zur Verfügung

```html
<!DOCTYPE html>
<html lang="de">
<head>
<meta charset="UTF-8">
<title>nordin lackwerk – Flyer Fliesenlack</title>
<link href="https://fonts.googleapis.com/css2?family=Open+Sans:wght@400;600;700&display=swap" rel="stylesheet">
<style>
  :root {
    --page-bg: #d9dadc;
    --brand-blue: #1d63ad;
    --brand-blue-deep: #0b4e93;
    --brand-blue-light: #3f86c9;
    --sheet-grey-top: #eceeef;
    --sheet-grey-bottom: #c9cdd0;
    --photo-light: #f3f4f4;
    --photo-mid: #e3e6e6;
    --photo-green: #6f9a8a;
    --accent-grey: #a9b7ba;
    --bullet-grey: #d6dadd;
    --text-grey: #4d5860;
    --tagline-grey: #556068;
    --white: #ffffff;
  }
  * { box-sizing: border-box; margin: 0; padding: 0; }
  html, body {
    width: 1200px; height: 900px; overflow: hidden;
    background: radial-gradient(ellipse at 50% 30%, #f2f2f3 0%, var(--page-bg) 75%);
    font-family: "Open Sans", Arial, sans-serif;
  }
  .canvas {
    width: 1200px; height: 900px;
    display: flex; justify-content: center; align-items: center; gap: 60px;
  }
  .flyer {
    width: 380px; height: 760px;
    padding: 70px 34px 30px;
    display: flex; flex-direction: column;
    box-shadow: 0 18px 40px rgba(0,0,0,.18);
  }
  .flyer--grey {
    background: linear-gradient(180deg, var(--sheet-grey-top) 0%, var(--sheet-grey-bottom) 100%);
    color: var(--brand-blue);
  }
  .flyer--blue {
    background: linear-gradient(180deg, var(--brand-blue-light) 0%, var(--brand-blue) 30%, var(--brand-blue-deep) 100%);
    color: var(--white);
  }
  .brand {
    font-size: 36px; font-weight: 700; line-height: 1.2;
  }
  .tagline {
    margin-top: 12px;
    font-size: 10px; font-weight: 700; letter-spacing: 1.4px; text-transform: uppercase;
    white-space: nowrap;
  }
  .flyer--grey .tagline { color: var(--tagline-grey); }
  .features { list-style: none; margin-top: 30px; display: flex; flex-direction: column; gap: 16px; }
  .features li {
    position: relative; padding-left: 24px;
    font-size: 12px; font-weight: 600; line-height: 1.3;
  }
  .features li::before {
    content: ""; position: absolute; left: 0; top: 2px;
    width: 11px; height: 11px;
  }
  .flyer--grey .features li { color: var(--text-grey); }
  .flyer--grey .features li::before { background: var(--brand-blue); }
  .flyer--blue .features li::before { background: var(--bullet-grey); }
  .product-visual {
    position: relative; margin: 24px -34px 0; height: 190px; flex-shrink: 0;
  }
  .product-visual__bar {
    position: absolute; right: 20px; top: 0; width: 32px; height: 140px;
    background: var(--accent-grey);
  }
  .product-visual__photo {
    position: absolute; left: 0; top: 26px; right: 40px; bottom: 0;
    background: linear-gradient(160deg, var(--photo-light) 0%, var(--photo-mid) 60%, var(--photo-green) 100%);
  }
  .product { margin-top: auto; font-weight: 600; }
  .product__name { font-size: 14px; letter-spacing: .5px; }
  .product__claim { margin-top: 8px; font-size: 13px; line-height: 1.4; }
</style>
</head>
<body>
<main class="canvas">

  <article class="flyer flyer--grey">
    <p class="brand">nordin lackwerk</p>
    <p class="tagline">Qualität vom Profi · zum günstigen Preis</p>
    <ul class="features">
      <li>Gelungene Wandsanierung durch hochwertige Fliesenfarbe</li>
      <li>2 Komponenten-Spritzlackfarbe auf Polyurethanharz-Kombi-Basis</li>
      <li>Bleifrei/chromatfrei</li>
      <li>Konsequente An- und Durchtrocknung</li>
      <li>Sehr gute Licht-, Kreidungs- und Wetterbeständigkeit</li>
      <li>In allen gängigen Spritzverfahren problemlos verarbeitbar</li>
    </ul>
    <div class="product-visual">
      <div class="product-visual__bar"></div>
      <div class="product-visual__photo" role="img" aria-label="Foto eines bunten Chamäleons auf hellem Grund"></div>
    </div>
    <div class="product">
      <p class="product__name">NORDIN 2 K - Fliesenlack</p>
      <p class="product__claim">wasserbasiert, lösemittelfrei<br>für alle Fliesen im senkrechten Bereich</p>
    </div>
  </article>

  <article class="flyer flyer--blue">
    <p class="brand">nordin lackwerk</p>
    <p class="tagline">Qualität vom Profi · zum günstigen Preis</p>
    <ul class="features">
      <li>Gelungene Wandsanierung durch hochwertige Fliesenfarbe</li>
      <li>2 Komponenten-Spritzlackfarbe auf Polyurethanharz-Kombi-Basis</li>
      <li>Bleifrei/chromatfrei</li>
      <li>Konsequente An- und Durchtrocknung</li>
      <li>Sehr gute Licht-, Kreidungs- und Wetterbeständigkeit</li>
      <li>In allen gängigen Spritzverfahren problemlos verarbeitbar</li>
    </ul>
    <div class="product-visual">
      <div class="product-visual__bar"></div>
      <div class="product-visual__photo" role="img" aria-label="Foto eines bunten Chamäleons auf hellem Grund"></div>
    </div>
    <div class="product">
      <p class="product__name">NORDIN 2 K - Fliesenlack</p>
      <p class="product__claim">wasserbasiert, lösemittelfrei<br>für alle Fliesen im senkrechten Bereich</p>
    </div>
  </article>

</main>
</body>
</html>
```